New web page design for our brand Casa Lunares

We have changed our logo and the image of our products, so we would like to redesign ,our web page as well according to the new design.
Our cosmetic products are based in nature and tradition, like they used to be prepared in the old pharmacies.
Our actual web is www.casalunaresweb.es, so we need similar estructure but completely different design.

Industry/Entity Type

Cosmetics

Number of Pages Required

5+ page

Requirements
Must have
• References to natural ingredients and also to old pharmacys or apothecaries.
Nice to have
• Nature images or old botanics drawings
• I would like to have a cover page with just an image saying welcome to Casa Lunares's world

```html
<!DOCTYPE html>
<html lang="en">
<head>
<meta charset="utf-8">
<title>Casa Lunares</title>
<link rel="stylesheet" href="https://fonts.googleapis.com/css2?family=Cinzel:wght@400;700&family=Libre+Baskerville:wght@400;700&family=Cormorant+Garamond:ital,wght@1,600&family=Open+Sans:wght@400;600;700&display=swap">
<style>
:root{
  --parchment:#dccaa3;
  --parchment-dark:#c6ab7c;
  --ink:#4a3625;
  --blue:#1d5fae;
  --blue-dark:#134787;
  --card:#ffffff;
  --text:#6b6258;
  --footer:#3b3028;
  --footer-bar:#2b231d;
  --footer-text:#cbbfae;
}
*{box-sizing:border-box;margin:0;padding:0}
html,body{width:1200px;height:2816px;overflow:hidden}
body{
  font-family:"Open Sans",sans-serif;color:var(--text);
  background:radial-gradient(ellipse at 50% 30%,#e6d7b6 0%,var(--parchment) 55%,var(--parchment-dark) 100%);
  position:relative;
}
.wrap{position:absolute;left:88px;width:1024px}
/* header */
.brand{position:absolute;top:18px;left:0;width:1200px;text-align:center;
  font-family:"Cinzel",serif;font-weight:700;font-size:44px;color:var(--ink);letter-spacing:2px}
.search{position:absolute;top:70px;right:88px;width:170px;height:26px;background:#fff;border:1px solid #b9a17a;display:flex;justify-content:flex-end;align-items:center;padding-right:6px}
.main-nav{top:176px;height:44px;background:linear-gradient(#2a71c4,var(--blue-dark));display:flex;align-items:center;padding-left:40px;gap:6px;border-radius:3px}
.main-nav a{color:#fff;text-decoration:none;font-size:14px;font-weight:700;padding:0 22px;height:44px;display:flex;align-items:center;gap:8px;letter-spacing:.5px}
.main-nav a.active{background:#fff;color:var(--blue);height:32px;border-radius:3px}
.main-nav .dot{width:7px;height:7px;background:#fff;border-radius:50%;opacity:.8}
/* hero */
.hero{top:224px;height:376px;overflow:hidden}
.hero-photo{position:absolute;inset:0;background:linear-gradient(120deg,#f4f2ea 0%,#e7e9e0 45%,#cfd8c0 70%,#9fb27c 100%)}
.hero-caption{position:absolute;left:0;right:0;bottom:0;height:46px;background:rgba(120,86,40,.72);
  font-family:"Cormorant Garamond",serif;font-style:italic;font-weight:600;color:#fff;font-size:22px;display:flex;align-items:center;justify-content:center}
.arrow{position:absolute;width:30px;height:30px;border-radius:50%;background:#4a3a2c;display:flex;align-items:center;justify-content:center}
/* welcome */
.welcome{top:600px;height:376px;background:var(--card);text-align:center;padding:52px 110px 0}
.welcome h1{font-family:"Cinzel",serif;font-size:34px;color:var(--blue);font-weight:400;letter-spacing:2px}
.rule{width:260px;height:2px;background:var(--parchment-dark);margin:18px auto 24px}
.welcome p{font-size:14px;line-height:24px}
.btn{display:inline-block;background:var(--blue);color:#fff;font-size:12px;font-weight:600;padding:7px 18px;border-radius:2px;text-decoration:none}
.welcome .btn{margin-top:20px}
/* section titles */
.section-title{display:flex;align-items:center;justify-content:center;gap:24px;font-family:"Cinzel",serif;font-size:34px;color:var(--ink);letter-spacing:2px}
.section-title::before,.section-title::after{content:"";width:150px;height:2px;background:var(--ink);opacity:.5}
/* products */
.products-title{top:1046px}
.row{display:flex;gap:16px}
.row-lg{top:1128px}
.row-sm{top:1672px}
.card{background:var(--card);flex:1;text-align:center;padding:12px 12px 18px;box-shadow:0 2px 6px rgba(70,50,30,.25)}
.card .photo{width:100%}
.row-lg .card{height:512px}
.row-lg .photo{height:250px}
.row-sm .card{height:416px}
.row-sm .photo{height:190px}
.card h3{font-family:"Libre Baskerville",serif;font-size:18px;color:var(--blue);font-weight:700;margin:18px 0 6px}
.card .line{width:120px;height:1px;background:#d6c8ae;margin:0 auto 12px}
.card p{font-size:12.5px;line-height:20px;margin-bottom:16px}
.card .btn{font-size:11px;padding:6px 16px}
/* news */
.news-title{top:2140px}
.news{top:2228px;height:270px;display:flex;gap:22px}
.news-item{flex:1;text-align:center}
.news-item .photo{height:150px;background:#fff;padding:8px;box-shadow:0 2px 6px rgba(70,50,30,.25)}
.news-item .photo div{width:100%;height:100%}
.news-item h4{font-family:"Libre Baskerville",serif;font-size:16px;color:var(--blue);line-height:22px;margin-top:14px}
.news-item time{font-size:12px;color:var(--ink);display:block;margin-top:6px}
/* footer */
.footer{position:absolute;left:0;top:2540px;width:1200px;height:238px;background:var(--footer);color:var(--footer-text);display:flex;gap:40px;padding:30px 88px 0}
.footer h5{color:#fff;font-size:15px;margin-bottom:14px}
.footer ul{list-style:none;font-size:13px;line-height:24px}
.footer ul li::before{content:"› ";color:#9c8d78}
.col{width:210px}
.col-news{width:300px}
.contact{font-size:13px;line-height:22px}
.contact strong{color:#fff}
.ci{display:flex;align-items:center;gap:8px}
.newsletter p{font-size:13px;line-height:20px;width:170px}
.signup{display:flex;margin-top:16px}
.signup span{flex:1;background:#fff;color:#999;font-size:12px;padding:8px 10px}
.signup b{background:var(--blue);color:#fff;font-size:12px;padding:8px 12px}
.social li{display:flex;align-items:center;gap:10px;line-height:30px}
.social li::before{content:none}
.social i{width:18px;height:18px;border-radius:50%;background:#7d6d5b;display:inline-block}
.bottom{position:absolute;left:0;top:2778px;width:1200px;height:38px;background:var(--footer-bar);color:var(--footer-text);font-size:12px;display:flex;align-items:center;justify-content:space-between;padding:0 88px}
</style>
</head>
<body>

<header>
  <div class="brand">Casa Lunares</div>
  <div class="search"><svg width="14" height="14" viewBox="0 0 14 14"><circle cx="6" cy="6" r="4.5" fill="none" stroke="#555" stroke-width="1.6"/><line x1="9.3" y1="9.3" x2="13" y2="13" stroke="#555" stroke-width="1.8"/></svg></div>
  <nav class="wrap main-nav">
    <a class="active" href="#">LAB ▾</a>
    <a href="#"><span class="dot"></span>PRODUCT LINES</a>
    <a href="#"><span class="dot"></span>SERVICES</a>
    <a href="#"><span class="dot"></span>NEWS</a>
    <a href="#"><span class="dot"></span>CONTACT</a>
    <a href="#"><span class="dot"></span>SHOP</a>
  </nav>
</header>

<section class="wrap hero">
  <div class="hero-photo" role="img" aria-label="Natural cream jars and a product box with green leaves"></div>
  <div class="hero-caption">Our cosmetic products are based in nature and tradition, like they used to be prepared in the old pharmacies.</div>
</section>
<div class="arrow" style="left:22px;top:396px"><svg width="12" height="12" viewBox="0 0 12 12"><path d="M8 1 3 6l5 5" fill="none" stroke="#fff" stroke-width="2"/></svg></div>
<div class="arrow" style="right:22px;top:396px"><svg width="12" height="12" viewBox="0 0 12 12"><path d="M4 1l5 5-5 5" fill="none" stroke="#fff" stroke-width="2"/></svg></div>

<section class="wrap welcome">
  <h1>WELCOME TO CASA LUNARES</h1>
  <div class="rule"></div>
  <p>Our remedies begin in the garden and the old apothecary shelf. Each cream, oil and balm is blended by hand in small batches, using herbs, flowers and minerals chosen for their gentle care. We keep the slow methods of the village pharmacy so that every jar feels honest, pure and kind to the skin.</p>
  <p>Welcome to a slower, gentler ritual.</p>
  <a class="btn" href="#">Read More</a>
</section>

<h2 class="wrap section-title products-title">OUR PRODUCTS</h2>

<section class="wrap row row-lg">
  <article class="card">
    <div class="photo" role="img" aria-label="Skincare portrait for the premium line" style="background:linear-gradient(135deg,#f3ece6,#e8d9cf)"></div>
    <h3>Premium Line</h3><div class="line"></div>
    <p>Gentle formulas with botanical extracts and pure oils, prepared in small batches to nourish and protect every type of skin, day after day.</p>
    <a class="btn" href="#">See More</a>
  </article>
  <article class="card">
    <div class="photo" role="img" aria-label="Baby care products for the children line" style="background:linear-gradient(135deg,#f7f4ef,#eadfd2)"></div>
    <h3>Children Line</h3><div class="line"></div>
    <p>Soft and mild care for the little ones, made with calendula, chamomile and sweet almond oil to soothe and comfort delicate skin gently.</p>
    <a class="btn" href="#">See More</a>
  </article>
  <article class="card">
    <div class="photo" role="img" aria-label="Natural soap, leaves and herbal ingredients" style="background:linear-gradient(135deg,#f2ece2,#b98a55 60%,#6f8a48)"></div>
    <h3>Natural Care</h3><div class="line"></div>
    <p>Plant based balms, soaps and oils inspired by traditional recipes, combining herbs and flowers to care for body and skin naturally.</p>
    <a class="btn" href="#">See More</a>
  </article>
</section>

<section class="wrap row row-sm">
  <article class="card">
    <div class="photo" role="img" aria-label="Nail treatment bottles" style="background:linear-gradient(135deg,#eef0ea,#c8d7c6)"></div>
    <h3>Nail Treatment</h3><div class="line"></div>
    <p>Natural care made with herbs and flowers, following the recipes of the old village pharmacy.</p>
    <a class="btn" href="#">See More</a>
  </article>
  <article class="card">
    <div class="photo" role="img" aria-label="Pharmacy product range on shelves" style="background:linear-gradient(135deg,#f2efe8,#d8cdb8)"></div>
    <h3 style="margin-top:10px">Recommendations Online Pharmacy</h3><div class="line"></div>
    <p>Natural care made with herbs and flowers, following the recipes of the old village pharmacy.</p>
    <a class="btn" href="#">See More</a>
  </article>
  <article class="card">
    <div class="photo" role="img" aria-label="Body treatment bottles with green labels" style="background:linear-gradient(135deg,#eef0e2,#a8bd78)"></div>
    <h3>Body Treatment</h3><div class="line"></div>
    <p>Natural care made with herbs and flowers, following the recipes of the old village pharmacy.</p>
    <a class="btn" href="#">See More</a>
  </article>
  <article class="card">
    <div class="photo" role="img" aria-label="Family health remedy bottles" style="background:linear-gradient(135deg,#f0ede4,#8a6a3e)"></div>
    <h3>Family Health</h3><div class="line"></div>
    <p>Natural care made with herbs and flowers, following the recipes of the old village pharmacy.</p>
    <a class="btn" href="#">See More</a>
  </article>
</section>

<h2 class="wrap section-title news-title">NEWS</h2>

<section class="wrap news">
  <article class="news-item"><div class="photo"><div role="img" aria-label="News photo of product jars" style="background:linear-gradient(135deg,#e6f0f4,#b9cfc2)"></div></div><h4>Lorem Ipsum Dolor Sit Amet con se Tetuer</h4><time>June 9, 2014</time></article>
  <article class="news-item"><div class="photo"><div role="img" aria-label="News photo of cosmetic range" style="background:linear-gradient(135deg,#eef2f6,#c3d3d8)"></div></div><h4>Lorem Ipsum Dolor Sit Amet con se Tetuer</h4><time>June 9, 2014</time></article>
  <article class="news-item"><div class="photo"><div role="img" aria-label="News photo of herbal bottles" style="background:linear-gradient(135deg,#eaf1f5,#b8cbb5)"></div></div><h4>Lorem Ipsum Dolor Sit Amet con se Tetuer</h4><time>June 9, 2014</time></article>
  <article class="news-item"><div class="photo"><div role="img" aria-label="News photo of cream jars" style="background:linear-gradient(135deg,#eef0f6,#c9c6dc)"></div></div><h4>Lorem Ipsum Dolor Sit Amet con se Tetuer</h4><time>June 9, 2014</time></article>
</section>
<div class="arrow" style="left:30px;top:2308px;background:none"><svg width="16" height="20" viewBox="0 0 16 20"><path d="M12 2 4 10l8 8" fill="none" stroke="#4a3a2c" stroke-width="3"/></svg></div>
<div class="arrow" style="right:30px;top:2308px;background:none"><svg width="16" height="20" viewBox="0 0 16 20"><path d="M4 2l8 8-8 8" fill="none" stroke="#4a3a2c" stroke-width="3"/></svg></div>

<footer class="footer">
  <div class="col">
    <h5>Quick Links</h5>
    <ul><li>Lab</li><li>Product Lines</li><li>Services</li><li>News</li><li>Contact</li><li>Shop</li></ul>
  </div>
  <div class="col contact">
    <h5>Contact Detail</h5>
    <strong>Casa Lunares</strong><br>
    C/ Jardín de la Botica 14<br>29001 Málaga, España<br>
    <div class="ci"><svg width="12" height="12" viewBox="0 0 12 12"><path d="M2 1h3l1 3-2 1a7 7 0 0 0 3 3l1-2 3 1v3c-6 1-10-3-9-9z" fill="#cbbfae"/></svg>+34 952 00 00 14</div>
    <div class="ci"><svg width="12" height="10" viewBox="0 0 12 10"><rect x=".5" y=".5" width="11" height="9" fill="none" stroke="#cbbfae"/><path d="M.5.5 6 5l5.5-4.5" fill="none" stroke="#cbbfae"/></svg>hola@casalunaresweb.es</div>
  </div>
  <div class="col-news newsletter">
    <h5>Newsletter Signup</h5>
    <div style="display:flex;align-items:center;justify-content:space-between">
      <p>Get the latest updates by subscribing to our newsletter</p>
      <svg width="60" height="44" viewBox="0 0 60 44"><path d="M2 22 58 2 40 42 28 28z" fill="#e9e2d6"/><path d="M28 28 58 2" stroke="#9c8d78" stroke-width="1.5"/></svg>
    </div>
    <div class="signup"><span>Enter your email here</span><b>SUBSCRIBE</b></div>
  </div>
  <div class="col">
    <h5>Follow Us</h5>
    <ul class="social"><li><i></i>LUNABOOK</li><li><i></i>CHIRPER</li><li><i></i>FRAMEGRAM</li><li><i></i>RSS FEED</li></ul>
  </div>
</footer>
<div class="bottom"><span>Copyright © 2014 CASA LUNARES. All Rights Reserved</span><span>Terms &amp; Conditions &nbsp;|&nbsp; Privacy Policy</span></div>

</body>
</html>
```